Sole Relationship Graphic of Chapter Organization for Book

This design shows relationships between variables associated with footwear and footprints. It will be used as a graphic in a book. The four elements of the graphic are (1) Variables, (2) Book Chapter Numbers (which correspond to the relationship(s) between at least two variables, (3) Relationship Arrows, and (4) Influence Arrows (because the influencers affect the variables differently than relationships between the variables). These names simply relate to the attempts I have made (and attached) at creating a graphic. In the attached diagrams, the circles with numbers are placeholders for the book chapter numbers, which may be changed so it will be good if I can change those after the graphic is completed. Chapter 1 will be the introduction.
The intent of of outsourcing this project is not necessarily sticking to the formats I have attached, but to allow your creativity to produce a useful graphic that can visually make the most sense of the relationships between the variables as chapters to readers of the book.

Target Market(s)

Search and Rescue Trackers

Requirements
Must have
• Information listed in project description, and drafted in attached diagrams
Nice to have
• Can include outlines of barefoot and outsoles. While Chapters 1 (Intro), 2 (Missing Persons' Footwear), 10 (Case Studies) and 11 (Summary) are set, the others aren't. The end game of this book is to use the rest of the variables to arrive at the end game, which is measurements for barefoot track length or outsole track length...so those two variables can be highlighted in some way to emphasize their importance.

```html
<!DOCTYPE html>
<html lang="en">
<head>
<meta charset="utf-8">
<title>Sole Relationship Chapter Map</title>
<link href="https://fonts.googleapis.com/css2?family=Baumans&display=swap" rel="stylesheet">
<style>
  :root {
    --teal: #40bfad;
    --teal-pale: #bfe9e2;
    --relation: #3f51a5;
    --influence: #f08a24;
    --paper: #ffffff;
    --label: #ffffff;
  }
  html, body {
    margin: 0;
    padding: 0;
    width: 1200px;
    height: 971px;
    overflow: hidden;
    background: var(--paper);
  }
  .chapter-map {
    display: block;
    width: 1200px;
    height: 971px;
  }
  .chapter-map text {
    font-family: "Baumans", "Comfortaa", sans-serif;
    text-anchor: middle;
    dominant-baseline: central;
  }
  .variable { fill: var(--teal); }
  .variable-label { fill: var(--label); font-size: 25px; }
  .variable-label.small { font-size: 21px; }
  .heading-label { fill: var(--label); font-size: 31px; }
  .brace { fill: none; stroke: var(--teal); stroke-width: 9; stroke-linecap: round; }
  .link { fill: none; stroke-width: 5; stroke-linecap: round; }
  .link.relation { stroke: var(--relation); }
  .link.influence { stroke: var(--influence); }
  .badge.relation { fill: var(--relation); }
  .badge.influence { fill: var(--influence); }
  .badge-number { fill: var(--label); font-size: 24px; }
  .legend-frame { fill: var(--paper); stroke: var(--teal); stroke-width: 5; }
  .legend-tab { fill: var(--teal); }
  .legend-title { fill: var(--label); font-size: 26px; }
  .legend-text { font-size: 23px; text-anchor: start !important; }
  .legend-text.chapter { fill: var(--teal); font-size: 26px; }
  .legend-text.relation { fill: var(--relation); }
  .legend-text.influence { fill: var(--influence); }
  .foot-outline { fill: var(--teal-pale); }
  .foot-solid { fill: var(--teal); }
</style>
</head>
<body>
<svg class="chapter-map" viewBox="0 0 1200 971" xmlns="http://www.w3.org/2000/svg">
  <defs>
    <marker id="head-relation" viewBox="0 0 12 12" refX="9" refY="6" markerWidth="5" markerHeight="5" orient="auto-start-reverse" markerUnits="strokeWidth">
      <polyline points="2,1 9,6 2,11" fill="none" stroke="#3f51a5" stroke-width="1.6" stroke-linecap="round" stroke-linejoin="round"/>
    </marker>
    <marker id="head-influence" viewBox="0 0 12 12" refX="9" refY="6" markerWidth="5" markerHeight="5" orient="auto-start-reverse" markerUnits="strokeWidth">
      <polyline points="2,1 9,6 2,11" fill="none" stroke="#f08a24" stroke-width="1.6" stroke-linecap="round" stroke-linejoin="round"/>
    </marker>
  </defs>

  <!-- Footwear heading and brace -->
  <ellipse class="variable" cx="484" cy="154" rx="128" ry="81"/>
  <text class="heading-label" x="484" y="117">MISSING</text>
  <text class="heading-label" x="484" y="154">PERSONS’</text>
  <text class="heading-label" x="484" y="192">FOOTWEAR</text>
  <path class="brace" d="M308 343 C330 280 370 272 420 276 C455 279 470 272 484 242 C498 272 513 279 548 276 C598 272 640 280 659 343"/>

  <!-- Outsole foot placeholder -->
  <ellipse class="foot-outline" role="img" aria-label="Outline of a bare foot sole" cx="194" cy="386" rx="48" ry="106" transform="rotate(14 194 386)"/>

  <!-- Variables -->
  <ellipse class="variable" cx="293" cy="419" rx="92" ry="56"/>
  <text class="variable-label" x="296" y="403">OUTSOLE</text>
  <text class="variable-label" x="298" y="435">LENGTH</text>

  <ellipse class="variable" cx="706" cy="419" rx="90" ry="56"/>
  <text class="variable-label" x="704" y="403">INSOLE</text>
  <text class="variable-label" x="706" y="435">LENGTH</text>

  <ellipse class="variable" cx="997" cy="419" rx="90" ry="56"/>
  <text class="variable-label" x="997" y="403">HOOK</text>
  <text class="variable-label" x="1000" y="435">AREA</text>

  <ellipse class="variable" cx="447" cy="597" rx="90" ry="56"/>
  <text class="variable-label" x="447" y="581">INDIVIDUAL</text>
  <text class="variable-label" x="450" y="613">VARIATION</text>

  <ellipse class="variable" cx="1009" cy="624" rx="90" ry="56"/>
  <text class="variable-label small" x="1009" y="609">BAREFOOT</text>
  <text class="variable-label small" x="1010" y="641">TRACK LENGTH</text>

  <ellipse class="variable" cx="160" cy="769" rx="90" ry="56"/>
  <text class="variable-label" x="160" y="737">SHOD</text>
  <text class="variable-label" x="160" y="769">TRACK</text>
  <text class="variable-label" x="160" y="801">LENGTH</text>

  <ellipse class="variable" cx="447" cy="791" rx="90" ry="56"/>
  <text class="variable-label" x="447" y="775">NOMINAL</text>
  <text class="variable-label" x="450" y="807">SIZE</text>

  <ellipse class="variable" cx="706" cy="791" rx="90" ry="56"/>
  <text class="variable-label" x="706" y="791">BAREFOOT</text>

  <ellipse class="variable" cx="1061" cy="791" rx="90" ry="56"/>
  <text class="variable-label" x="1061" y="791">HEIGHT</text>

  <!-- Barefoot foot placeholder -->
  <ellipse class="foot-solid" role="img" aria-label="Solid silhouette of a bare foot" cx="815" cy="768" rx="34" ry="102" transform="rotate(-4 815 768)"/>

  <!-- Relationship arrows -->
  <line class="link relation" x1="401" y1="411" x2="597" y2="411" marker-start="url(#head-relation)" marker-end="url(#head-relation)"/>
  <line class="link relation" x1="174" y1="700" x2="281" y2="486" marker-end="url(#head-relation)"/>
  <line class="link relation" x1="503" y1="735" x2="670" y2="484" marker-end="url(#head-relation)"/>
  <line class="link relation" x1="712" y1="497" x2="712" y2="722" marker-start="url(#head-relation)" marker-end="url(#head-relation)"/>
  <line class="link relation" x1="545" y1="792" x2="606" y2="792" marker-end="url(#head-relation)"/>
  <line class="link relation" x1="961" y1="795" x2="871" y2="795" marker-end="url(#head-relation)"/>
  <line class="link relation" x1="850" y1="690" x2="914" y2="648" marker-end="url(#head-relation)"/>

  <!-- Influence arrows -->
  <line class="link influence" x1="897" y1="411" x2="806" y2="411" marker-end="url(#head-influence)"/>
  <line class="link influence" x1="395" y1="541" x2="338" y2="482" marker-end="url(#head-influence)"/>
  <line class="link influence" x1="529" y1="555" x2="623" y2="462" marker-end="url(#head-influence)"/>
  <line class="link influence" x1="445" y1="661" x2="445" y2="726" marker-end="url(#head-influence)"/>

  <!-- Chapter badges -->
  <g class="chapter-badges">
    <circle class="badge relation" cx="492" cy="410" r="18"/><text class="badge-number" x="492" y="410">5</text>
    <circle class="badge influence" cx="861" cy="411" r="18"/><text class="badge-number" x="861" y="411">3</text>
    <circle class="badge relation" cx="216" cy="605" r="18"/><text class="badge-number" x="216" y="605">6</text>
    <circle class="badge influence" cx="374" cy="516" r="18"/><text class="badge-number" x="374" y="516">7</text>
    <circle class="badge influence" cx="561" cy="521" r="18"/><text class="badge-number" x="561" y="521">7</text>
    <circle class="badge relation" cx="569" cy="632" r="18"/><text class="badge-number" x="569" y="632">4</text>
    <circle class="badge relation" cx="712" cy="606" r="18"/><text class="badge-number" x="712" y="606">9</text>
    <circle class="badge influence" cx="445" cy="686" r="18"/><text class="badge-number" x="445" y="686">5</text>
    <circle class="badge relation" cx="568" cy="792" r="18"/><text class="badge-number" x="568" y="792">4</text>
    <circle class="badge relation" cx="921" cy="793" r="18"/><text class="badge-number" x="921" y="793">8</text>
    <circle class="badge relation" cx="877" cy="674" r="18"/><text class="badge-number" x="877" y="674">9</text>
  </g>

  <!-- Legend -->
  <g class="legend">
    <rect class="legend-frame" x="724" y="91" width="349" height="189" rx="10"/>
    <rect class="legend-tab" x="824" y="74" width="148" height="36" rx="10"/>
    <text class="legend-title" x="898" y="92">LEGEND</text>
    <circle class="badge" fill="var(--teal)" cx="770" cy="145" r="18"/>
    <text class="badge-number" x="770" y="145">1</text>
    <text class="legend-text chapter" x="799" y="146">CHAPTER #</text>
    <line class="link relation" x1="777" y1="197" x2="828" y2="197" marker-end="url(#head-relation)"/>
    <text class="legend-text relation" x="840" y="198">RELATIONSHIP TO</text>
    <line class="link influence" x1="777" y1="243" x2="828" y2="243" marker-end="url(#head-influence)"/>
    <text class="legend-text influence" x="840" y="244">INFLUENCE ON</text>
  </g>
</svg>
</body>
</html>
```